Baby acupressure app for parents

We need an app for parents that teaches parents how to help them relieve their baby's imbalances (stomach ache, trouble sleeping etc.)

Please see the attached document (with info) and wireframes.

This project is urgent so please only participate if you're able to finish all screens within a few days after the contest is over.

Target Market(s)

Baby moms (20-40 years of age)

Industry/Entity Type

Baby Care

Colors
886aae
b768aa
e667a6
f68d4d
faa54b
fac994
f9ba93
f59195
fee18a

Requirements
Must have
• A high quality design that is both modern and very sleek and stylish.
Nice to have
• Simple animations to make the app "feel" like it's extreme high quality and make the user want to use it again and again
Should not have
• Sandwich menus

```html
<!DOCTYPE html>
<html lang="en">
<head>
<meta charset="utf-8">
<title>Mild Mave – Home</title>
<link rel="stylesheet" href="https://fonts.googleapis.com/css2?family=Montserrat:wght@300;400;700&display=swap">
<style>
  :root {
    --top-pink: #c86a9f;
    --mid-violet: #a163ad;
    --band-purple: #8452b4;
    --photo-light: #e9e4e0;
    --photo-warm: #d9cbc2;
    --white: #ffffff;
    --tab-ink: #9a5cb0;
    --play-ink: #8f55b4;
  }
  * { margin: 0; padding: 0; box-sizing: border-box; }
  html, body { width: 800px; height: 1200px; overflow: hidden; }
  body { font-family: "Montserrat", sans-serif; background: var(--white); }
  .screen { position: relative; width: 800px; height: 1200px; overflow: hidden; }

  .intro {
    position: absolute; left: 0; top: 0; width: 800px; height: 575px;
    background: linear-gradient(180deg, var(--top-pink) 0%, var(--mid-violet) 100%);
    color: var(--white); padding: 0 27px;
  }
  .intro-title {
    font-weight: 300; font-size: 57px; text-align: center;
    margin-top: 68px; line-height: 70px; letter-spacing: 0.5px;
  }
  .intro-text {
    font-weight: 300; font-size: 29px; line-height: 39px; margin-top: 14px;
    letter-spacing: 0.2px; white-space: nowrap;
  }
  .intro-text + .intro-text { margin-top: 39px; }
  .intro-cta { font-weight: 300; font-size: 29px; line-height: 39px; margin-top: 32px; white-space: nowrap; }
  .intro-cta strong { font-weight: 700; }

  .video {
    position: absolute; left: 0; top: 575px; width: 800px; height: 500px;
  }
  .video-still {
    position: absolute; inset: 0;
    background: radial-gradient(ellipse at 55% 45%, #f4ebe6 0%, var(--photo-warm) 45%, var(--photo-light) 100%);
  }
  .video-curve { position: absolute; left: 0; top: 0; }
  .play-button {
    position: absolute; left: 340px; top: 161px; width: 120px; height: 120px;
    border-radius: 50%; background: var(--white);
  }
  .play-button svg { position: absolute; left: 48px; top: 44px; }

  .tab-bar {
    position: absolute; left: 0; top: 1075px; width: 800px; height: 125px;
    background: var(--white);
  }
  .tab {
    position: absolute; top: 26px; width: 180px; margin-left: -90px;
    display: flex; flex-direction: column; align-items: center;
    color: var(--tab-ink); font-size: 20px; font-weight: 400; line-height: 24px;
  }
  .tab svg { height: 52px; margin-bottom: 9px; }
</style>
</head>
<body>
<main class="screen">
  <section class="intro">
    <h1 class="intro-title">Mild Mave</h1>
    <p class="intro-text">Lorem ipsum dolor sit amet, consectetuer<br>adipiscing elit, sed diam nonummy nibh euismod<br>tincidunt ut laoreet dolore magna aliquam erat<br>volutpat. Ut wisi enim ad minim veniam.</p>
    <p class="intro-text">Lorem ipsum dolor sit amet, consectetuer<br>adipiscing elit, sed diam nonummy nibh euismod<br>tincidunt ut laoreet dolore magna.</p>
    <p class="intro-cta">Select <strong>“imbalances”</strong> in the menu to get started!</p>
  </section>

  <section class="video">
    <div class="video-still" role="img" aria-label="Photo of a sleeping newborn wrapped in a white blanket on a knitted throw"></div>
    <svg class="video-curve" width="800" height="500" viewBox="0 0 800 500">
      <path d="M0 410 Q400 490 800 410 L800 500 L0 500 Z" fill="var(--band-purple)"/>
    </svg>
    <div class="play-button" aria-label="Play video">
      <svg width="30" height="32" viewBox="0 0 30 32"><path d="M0 0 L28 16 L0 32 Z" fill="var(--play-ink)"/></svg>
    </div>
  </section>

  <nav class="tab-bar">
    <div class="tab" style="left:119px">
      <svg viewBox="0 0 56 52" width="56"><path d="M4 26 L28 3 L52 26 M10 20 V49 H22 V33 H34 V49 H46 V20" fill="none" stroke="currentColor" stroke-width="2.2" stroke-linejoin="round"/></svg>
      <span>Home</span>
    </div>
    <div class="tab" style="left:306px">
      <svg viewBox="0 0 56 52" width="56"><path d="M30 3 H51 V24 L24 50 L4 30 Z" fill="none" stroke="currentColor" stroke-width="2.2" stroke-linejoin="round"/><circle cx="42" cy="12" r="3.5" fill="none" stroke="currentColor" stroke-width="2.2"/></svg>
      <span>Imbalances</span>
    </div>
    <div class="tab" style="left:494px">
      <svg viewBox="0 0 56 52" width="56"><path d="M22 16 H4 V49 H46 V36" fill="none" stroke="currentColor" stroke-width="2.2"/><path d="M14 38 C16 24 26 18 38 18 V26 L53 13 L38 1 V9 C24 9 14 20 14 38 Z" fill="none" stroke="currentColor" stroke-width="2.2" stroke-linejoin="round"/></svg>
      <span>Share</span>
    </div>
    <div class="tab" style="left:681px">
      <svg viewBox="0 0 56 52" width="56"><circle cx="28" cy="26" r="24" fill="none" stroke="currentColor" stroke-width="2.2"/><circle cx="28" cy="15" r="2" fill="currentColor"/><path d="M28 22 V38" stroke="currentColor" stroke-width="2.4"/></svg>
      <span>About</span>
    </div>
  </nav>
</main>
</body>
</html>
```